Marlowe Lane Quilts

We are opening a long-arm quilting business where customers will bring in their pieced quilt top and have us quilt it to the batting and backing. We own a Brevant Orlix Framer - photos can be found on the internet. We would like for our business card and logo to include an image of a long arm quilting machine so that our business type would be easily recognizable. We like lots of color and contemporary styling, perhaps with colorful fabric flowing on the card as well. It needs to be something transferable to a store window and/or to a decal for our car to aid in advertising.

Industry/Entity Type

Store

Colors
fff5ee
fde8d3

```html
<!DOCTYPE html>
<html lang="en">
<head>
<meta charset="utf-8">
<title>Marlowe Lane Quilts – Business Card</title>
<link href="https://fonts.googleapis.com/css2?family=Open+Sans:wght@400;600&display=swap" rel="stylesheet">
<style>
  :root {
    --backdrop: #e4e4e4;
    --card: #ffffff;
    --orange: #f8a61c;
    --green: #8cc63f;
    --blue: #27a6df;
    --ink: #222222;
    --machine-light: #f1f1f1;
    --machine-dark: #5a5048;
  }
  * { box-sizing: border-box; margin: 0; padding: 0; }
  html, body {
    width: 1200px;
    height: 900px;
    overflow: hidden;
    background: var(--backdrop);
    font-family: "Open Sans", Arial, sans-serif;
  }
  .business-card {
    position: absolute;
    left: 80px;
    top: 130px;
    width: 1040px;
    height: 640px;
    background: var(--card);
    border-radius: 36px;
    overflow: hidden;
    box-shadow: 0 10px 30px rgba(0,0,0,0.18);
  }
  .swooshes {
    position: absolute;
    inset: 0;
    width: 1040px;
    height: 640px;
  }
  .owners {
    position: absolute;
    right: 44px;
    top: 70px;
    text-align: right;
    color: var(--ink);
    font-size: 22px;
    line-height: 1.35;
  }
  .owners .role {
    color: var(--blue);
    font-size: 18px;
  }
  .brand-name {
    position: absolute;
    left: 170px;
    top: 190px;
    color: var(--orange);
    font-size: 58px;
    line-height: 1.2;
    font-weight: 400;
    letter-spacing: 0.5px;
    white-space: nowrap;
  }
  .machine-photo {
    position: absolute;
    left: 700px;
    top: 290px;
    width: 320px;
    height: 270px;
    border-radius: 6px;
    background: linear-gradient(160deg, var(--machine-light) 0%, #c9c2ba 55%, var(--machine-dark) 100%);
  }
  .contact-list {
    position: absolute;
    left: 60px;
    top: 430px;
    list-style: none;
    color: var(--ink);
    font-size: 30px;
    line-height: 44px;
  }
  .contact-list li {
    display: flex;
    align-items: center;
    gap: 10px;
  }
  .contact-list svg {
    width: 32px;
    height: 32px;
    flex: none;
  }
</style>
</head>
<body>
  <main class="business-card">
    <svg class="swooshes" viewBox="0 0 1040 640" aria-hidden="true">
      <path fill="var(--orange)" d="M0,0 H560 C420,15 200,30 0,110 Z"/>
      <path fill="var(--green)" d="M0,110 C200,30 420,15 560,0 H620 C430,25 210,55 0,140 Z"/>
      <path fill="var(--blue)" d="M0,140 C210,55 430,25 620,0 H780 C560,20 260,75 0,175 Z"/>
      <path fill="var(--orange)" d="M1040,640 H560 C760,620 920,560 1040,470 Z"/>
      <path fill="var(--blue)" d="M1040,470 C920,560 760,620 560,640 H430 C680,610 880,520 1040,392 Z"/>
      <path fill="var(--green)" d="M430,640 C680,610 880,520 1040,392 V360 C870,500 640,600 300,640 Z"/>
    </svg>

    <div class="owners">
      <p>Daniel Ashcroft &amp;<br>Lena Whitfield</p>
      <p class="role">Owners</p>
    </div>

    <h1 class="brand-name">Marlowe Lane Quilts</h1>

    <div class="machine-photo" role="img" aria-label="Photo of a long-arm quilting machine on its frame"></div>

    <ul class="contact-list">
      <li>
        <svg viewBox="0 0 24 24" aria-hidden="true"><path fill="var(--blue)" d="M6.6 10.8a15 15 0 0 0 6.6 6.6l2.2-2.2c.3-.3.7-.4 1-.2 1.1.4 2.3.6 3.6.6.6 0 1 .4 1 1V20c0 .6-.4 1-1 1A17 17 0 0 1 3 4c0-.6.4-1 1-1h3.5c.6 0 1 .4 1 1 0 1.3.2 2.5.6 3.6.1.3 0 .7-.2 1z"/></svg>
        <span>555.210.4836</span>
      </li>
      <li>
        <svg viewBox="0 0 24 24" aria-hidden="true"><g fill="none" stroke="var(--blue)" stroke-width="2"><circle cx="12" cy="12" r="9.5"/><ellipse cx="12" cy="12" rx="4" ry="9.5"/><path d="M2.5 12h19M4 7h16M4 17h16"/></g></svg>
        <span>www.marlowelanequilts.com</span>
      </li>
      <li>
        <svg viewBox="0 0 24 24" aria-hidden="true"><rect x="2" y="5" width="20" height="14" rx="2" fill="var(--blue)"/><path d="M3 6l9 7 9-7" fill="none" stroke="#fff" stroke-width="1.8"/></svg>
        <span>marlowelanequilts@mailbox.com</span>
      </li>
      <li>
        <svg viewBox="0 0 24 24" aria-hidden="true"><path fill="var(--blue)" d="M12 3 1.5 12H5v9h5.5v-6h3v6H19v-9h3.5z"/></svg>
        <span>418 Harbor Street, Calden, CA 95012</span>
      </li>
    </ul>
  </main>
</body>
</html>
```